personal one page website

personal one page site. based on details available on www.drlucasferrow.com
design needs to show:
- unique background of doctor
- serving high value customer group
- non-profit work
if you would compare the professional life of DrLucasFerrow with other brands:
a car: it would be velmor crade
a watch: it would be Quorin Velsaud
a sport: horse polo
a sports gear company: zolt
a drink: macha green tea
a city: Tokyo
the visitor of the site should have the following impressions (in chronological order):
1. Beautiful
2. Interesting
3. this person is a good example for others
4. what will be next ?
www.drlucasferrow.com
the main colors should be black / white / grey scales. thank you (including photos).
dear all. the site serves information purpose only and is non-commercial (no phone, appointment, chirp ,fb on the site). you can look at it as an 'online-CV'. no link to the company site 'harbimedic.com'
Dear All,

```html
<!DOCTYPE html>
<html lang="en">
<head>
<meta charset="utf-8">
<title>Doctor Lucas A Ferrow, PhD — Dental Surgery</title>
<link href="https://fonts.googleapis.com/css2?family=Raleway:wght@400;500;600;700;800&family=Open+Sans:wght@400;600&display=swap" rel="stylesheet">
<style>
:root{
  --blue:#2f7fc1;
  --blue-dark:#24669d;
  --ink:#ffffff;
  --muted:#9a9a9a;
  --dim:#6f6f6f;
  --bg-page:#252525;
  --bg-band:#333333;
  --bg-deep:#161616;
  --bg-nav:#1c1c1c;
  --line:#444444;
}
*{box-sizing:border-box;margin:0;padding:0}
html,body{width:1200px;height:4865px;overflow:hidden}
body{background:var(--bg-page);color:var(--ink);font-family:"Open Sans",Arial,sans-serif;position:relative}
.abs{position:absolute}
h1,h2,h3,h4{font-family:"Raleway",Helvetica,sans-serif}

/* hero */
.hero{left:0;top:0;width:1200px;height:525px;background:radial-gradient(ellipse at 70% 30%,#8c8580 0%,#5a5450 40%,#2e2c2b 100%)}
.hero-kicker{left:0;top:200px;width:1200px;text-align:center;color:var(--blue);font-family:"Raleway",sans-serif;font-size:42px;font-weight:700}
.hero-title{left:0;top:250px;width:1200px;text-align:center;font-size:62px;font-weight:800}
.hero-actions{left:0;top:363px;width:1200px;display:flex;justify-content:center;gap:12px}
.btn{font-family:"Raleway",sans-serif;font-size:14px;font-weight:600;padding:10px 22px;border:2px solid #fff;color:#fff;background:rgba(0,0,0,.35)}
.btn-primary{background:var(--blue-dark);border-color:var(--blue)}

/* nav */
.nav{left:0;top:525px;width:1200px;height:59px;background:var(--bg-nav);border-bottom:1px solid #111}
.nav-brand{left:90px;top:20px;font-family:"Raleway",sans-serif;font-size:15px;font-weight:600;color:#ddd}
.nav-menu{right:86px;top:0;display:flex;list-style:none;height:59px;align-items:center;gap:26px}
.nav-menu li{font-family:"Raleway",sans-serif;font-size:12px;font-weight:600;color:#bbb;padding:6px 0}
.nav-menu li.active{color:#fff;border-bottom:2px solid var(--blue)}

/* section bands */
.band{left:0;width:1200px;height:96px;background:var(--bg-band)}
.band-title{left:81px;top:18px;font-size:36px;font-weight:800;color:#5b5b5b}
.band-sub{left:81px;top:58px;font-size:13px;color:#ddd}

/* about */
.about-photo{left:81px;top:707px;width:243px;height:240px;background:linear-gradient(160deg,#d9d9d9,#8d8d8d)}
.about-name{left:81px;top:947px;width:243px;height:91px;background:var(--blue);text-align:center;padding-top:20px}
.about-name h3{font-size:18px;font-weight:700}
.about-name p{font-size:14px;color:#dce9f5;margin-top:6px}
.about-text{left:347px;top:702px;width:772px;font-size:13px;line-height:20px;color:var(--muted)}
.about-cols{left:347px;top:810px;width:772px;height:230px;display:flex}
.about-col{flex:1;text-align:center;border-right:1px solid var(--line)}
.about-col:last-child{border-right:0}
.about-col svg{margin-top:24px}
.about-col h4{color:var(--blue);font-size:14px;font-weight:700;margin:18px 0 14px}
.about-col p{font-size:13px;line-height:22px;color:var(--muted)}
.about-col b{color:#ddd;font-weight:600}

/* quote band */
.quote-band{left:0;top:1119px;width:1200px;height:178px;background:linear-gradient(90deg,#3a3a3a,#6b6b6b 55%,#3a3a3a)}
.quote-text{left:0;top:1196px;width:1200px;text-align:center;color:var(--blue);font-size:14px;font-weight:600;padding:0 120px}
.journey-label{left:81px;top:1318px;font-family:"Raleway",sans-serif;font-size:13px;font-weight:600;color:#ddd}

/* timeline */
.timeline{left:0;top:1356px;width:1200px;height:1336px;background:#2a2a2a}
.section-head{left:0;width:1200px;display:flex;justify-content:center;align-items:center;gap:18px;color:var(--blue);font-family:"Raleway",sans-serif;font-size:14px;font-weight:700}
.section-head::before,.section-head::after{content:"";width:60px;height:1px;background:var(--blue)}
.tl-line{left:122px;width:2px;background:#555}
.tl-item{left:81px;width:1038px}
.tl-date{position:absolute;left:0;top:0;width:81px;height:28px;background:var(--blue);text-align:center;font-size:12px;line-height:28px}
.tl-body{position:absolute;left:101px;top:-4px;width:937px}
.tl-body h3{font-size:21px;font-weight:700}
.tl-body .sub{font-size:13px;color:var(--dim);margin-top:4px}
.tl-body p{font-size:13px;line-height:20px;color:var(--muted);margin-top:6px}
.tl-body a{color:var(--blue);text-decoration:none}
.btn-outline{left:500px;top:1737px;width:200px;height:48px;border:2px solid #ddd;text-align:center;line-height:44px;font-family:"Raleway",sans-serif;font-size:15px;font-weight:600}

/* gallery */
.gallery-bg{left:0;top:2692px;width:1200px;height:1200px;background:#2a2a2a}
.filters{left:0;top:2916px;width:1200px;display:flex;justify-content:center;gap:8px}
.filters span{font-size:11px;color:#888;background:#3a3a3a;padding:6px 14px}
.filters span.on{background:var(--blue);color:#fff}
.grid{left:0;top:2977px;width:1200px;display:grid;grid-template-columns:repeat(5,240px);grid-auto-rows:242px}
.tile:nth-child(3n+1){background:linear-gradient(150deg,#7d7a77,#3f3d3c)}
.tile:nth-child(3n+2){background:linear-gradient(150deg,#5d6a78,#2f3238)}
.tile:nth-child(3n){background:linear-gradient(150deg,#a39b90,#55504a)}
.load-more{left:520px;top:3752px;width:160px;height:50px;background:var(--blue);text-align:center;line-height:50px;font-family:"Raleway",sans-serif;font-size:15px;font-weight:600}

/* testimonial */
.testimonial{left:0;top:3892px;width:1200px;height:340px;background:var(--bg-deep)}
.t-quote{left:0;top:4010px;width:1200px;text-align:center;font-size:17px;color:#eee}
.avatar{left:570px;top:4063px;width:60px;height:60px;background:linear-gradient(160deg,#c9c9c9,#777)}
.t-name{left:0;top:4136px;width:1200px;text-align:center;font-family:"Raleway",sans-serif;font-size:18px;font-weight:700}
.t-role{left:0;top:4166px;width:1200px;text-align:center;font-size:13px;color:var(--blue)}

/* contact */
.contact-bg{left:0;top:4328px;width:1200px;height:472px;background:#1e1e1e}
.contact-info{left:81px;top:4450px;width:490px;font-size:13px;line-height:20px;color:var(--muted)}
.contact-list{left:81px;top:4524px;display:grid;grid-template-columns:70px auto;font-size:13px;line-height:21px;color:#ddd}
.contact-list dd{color:var(--blue)}
.form label{position:absolute;font-size:13px;color:#ddd}
.field{position:absolute;height:1px;background:#555}
.textarea{position:absolute;border:1px solid #555}

/* footer */
.footer{left:0;top:4800px;width:1200px;height:65px;background:var(--blue)}
.footer p{position:absolute;left:81px;top:24px;font-size:12px;color:#e6f0fa}
.footer-links{position:absolute;right:81px;top:24px;display:flex;gap:22px}
.footer-links i{display:block;width:14px;height:14px;border-radius:50%;background:#e6f0fa}
</style>
</head>
<body>

<header>
  <div class="abs hero" role="img" aria-label="Portrait photograph of the doctor in a clinic, softly darkened"></div>
  <p class="abs hero-kicker">Doctor Lucas A Ferrow, PhD</p>
  <h1 class="abs hero-title">Dental Surgery</h1>
  <div class="abs hero-actions"><span class="btn">About</span><span class="btn btn-primary">Download VCARD</span></div>
</header>

<nav class="abs nav">
  <span class="abs nav-brand">Dr Lucas A Ferrow</span>
  <ul class="abs nav-menu">
    <li class="active">HOME</li><li>ABOUT</li><li>AWARDS</li><li>SCIENTIFIC PUBLICATIONS</li><li>NEWS/MEDIA</li><li>CONTACT</li>
  </ul>
</nav>

<section class="about">
  <div class="abs band" style="top:584px">
    <h2 class="abs band-title">ABOUT ME</h2>
    <p class="abs band-sub">A LITTLE STORY ABOUT WHAT I DO IN MY LIFE</p>
  </div>
  <div class="abs about-photo" role="img" aria-label="Portrait photograph of the doctor in shirt and tie"></div>
  <div class="abs about-name"><h3>Dr. Lucas A Ferrow</h3><p>Dental Surgery</p></div>
  <p class="abs about-text">Lorem ipsum dolor sit amet, consectetur adipiscing elit, sed do eiusmod tempor incididunt ut labore et dolore magna aliqua. Ut enim ad minim veniam, quis nostrud exercitation ullamco laboris nisi ut aliquip ex ea commodo consequat. Duis aute irure dolor in reprehenderit in voluptate velit esse cillum dolore eu fugiat nulla pariatur, ullamco laboris nisi ut aliquip ex ea commodo consequat. Duis aute irure dolor in reprehenderit in voluptate velit esse cillum dolore eu fugiat nulla pariatur.</p>
  <div class="abs about-cols">
    <div class="about-col">
      <svg width="64" height="64" viewBox="0 0 64 64" aria-hidden="true"><circle cx="32" cy="20" r="13" fill="#bbb"/><path d="M8 62c0-16 11-24 24-24s24 8 24 24z" fill="#bbb"/></svg>
      <h4>PERSONAL INFO</h4>
      <p><b>position :</b> Lorem ipsum<br><b>birth :</b> Lorem ipsum<br><b>hobby :</b> Lorem ipsum</p>
    </div>
    <div class="about-col">
      <svg width="64" height="64" viewBox="0 0 64 64" aria-hidden="true"><rect x="4" y="14" width="56" height="38" fill="#bbb"/><path d="M4 14l28 22 28-22" fill="none" stroke="#252525" stroke-width="3"/></svg>
      <h4>CONTACT</h4>
      <p><b>email :</b> admin@drlucasferrow.com<br><b>phone :</b> +0(0)00 000 000<br><b>callnet :</b> drlucasferrow</p>
    </div>
    <div class="about-col">
      <svg width="64" height="64" viewBox="0 0 64 64" aria-hidden="true" fill="none" stroke="#bbb" stroke-width="4"><rect x="24" y="4" width="16" height="14"/><rect x="4" y="44" width="16" height="14"/><rect x="44" y="44" width="16" height="14"/><path d="M32 18v12M12 44V30h40v14"/></svg>
      <h4>SOCIAL MEDIA</h4>
      <p><b>chirp :</b> @drlucas<br><b>facelog :</b> drlucasferrow<br><b>postly :</b> drlucasferrow</p>
    </div>
  </div>
</section>

<div class="abs quote-band" role="img" aria-label="Close-up photograph of stacked book pages in grey tones"></div>
<p class="abs quote-text">Dr Lucas A Ferrow graduated as a dentist in lingual orthodontics and later joined a team of specialists serving patients worldwide.</p>
<p class="abs journey-label">A LITTLE JOURNEY OF MY LIFE</p>

<section>
  <div class="abs timeline"></div>
  <div class="abs tl-line" style="top:1470px;height:1190px"></div>
  <h2 class="abs section-head" style="top:1410px">Scientific Publications</h2>

  <div class="abs tl-item" style="top:1473px"><span class="tl-date">2008</span>
    <div class="tl-body"><h3>Review of Lingual Orthodontics</h3><p class="sub">Self-ligating brackets in lingual orthodontics with full indication</p>
    <p>At vero eos et accusamus et iusto odio dignissimos ducimus qui blanditiis praesentium voluptatum deleniti atque corrupti quos dolores et quas molestias excepturi sint. Lorem ipsum dolor sit amet, sed do eiusmod tempor incididunt ut labore et dolore magna aliqua. <a>Read the Article</a></p></div></div>

  <div class="abs tl-item" style="top:1619px"><span class="tl-date">2009</span>
    <div class="tl-body"><h3>Halden School of Dental Medicine</h3><p class="sub">Dental education in practice</p>
    <p>At vero eos et accusamus et iusto odio dignissimos ducimus qui blanditiis praesentium voluptatum deleniti atque corrupti quos dolores et quas molestias excepturi sint. <a>Read the Article</a></p></div></div>

  <div class="abs btn-outline">Other Publications</div>

  <h2 class="abs section-head" style="top:1848px">Academic Degree and Specializations</h2>

  <div class="abs tl-item" style="top:1908px"><span class="tl-date">2005</span>
    <div class="tl-body"><h3>PhD in Orthodontics / Dentofacial Orthopaedics</h3><p class="sub">West Germany</p>
    <p>Lorem ipsum dolor sit amet, consectetur adipiscing elit, sed do eiusmod tempor incididunt ut labore et dolore magna aliqua. Ut enim ad minim veniam, quis nostrud exercitation ullamco laboris nisi ut aliquip ex ea commodo consequat. Duis aute irure dolor in reprehenderit in voluptate velit esse cillum dolore eu fugiat nulla pariatur.</p></div></div>

  <div class="abs tl-item" style="top:2047px"><span class="tl-date">2005</span>
    <div class="tl-body"><h3>Fachzahnarzt für Kieferorthopädie</h3><p class="sub">Hamburg, North Germany</p>
    <p>At vero eos et accusamus et iusto odio dignissimos ducimus qui blanditiis praesentium voluptatum deleniti atque corrupti quos dolores et quas molestias excepturi sint.</p></div></div>

  <div class="abs tl-item" style="top:2174px"><span class="tl-date">2005</span>
    <div class="tl-body"><h3>Specialist in Lingual Orthodontics (DUOL)</h3>
    <p>At vero eos et accusamus et iusto odio dignissimos ducimus qui blanditiis praesentium voluptatum deleniti atque corrupti quos dolores et quas molestias excepturi sint.</p></div></div>

  <div class="abs tl-item" style="top:2274px"><span class="tl-date">2005</span>
    <div class="tl-body"><h3>Diplome Universitaire d'Orthodontie Lingua</h3><p class="sub">Paris, France</p>
    <p>At vero eos et accusamus et iusto odio dignissimos ducimus qui blanditiis praesentium voluptatum deleniti atque corrupti quos dolores et quas molestias excepturi sint.</p></div></div>

  <div class="abs tl-item" style="top:2401px"><span class="tl-date">2005</span>
    <div class="tl-body"><h3>Halden Alumnus</h3><p class="sub">United States</p>
    <p>At vero eos et accusamus et iusto odio dignissimos ducimus qui blanditiis praesentium voluptatum deleniti atque corrupti quos dolores et quas molestias excepturi sint.</p></div></div>

  <div class="abs tl-item" style="top:2534px"><span class="tl-date">2005</span>
    <div class="tl-body"><h3>Certificate in Oral Implantology</h3><p class="sub">Level 1, 2<br>United States</p>
    <p>At vero eos et accusamus et iusto odio dignissimos ducimus qui blanditiis praesentium voluptatum deleniti atque corrupti quos dolores et quas molestias excepturi sint.</p></div></div>
</section>

<section>
  <div class="abs gallery-bg"></div>
  <div class="abs band" style="top:2757px">
    <h2 class="abs band-title">Gallery</h2>
    <p class="abs band-sub">What to do, what I am about</p>
  </div>
  <div class="abs filters"><span class="on">All</span><span>Work</span><span>Travel</span><span>Events</span><span>Charity</span></div>
  <div class="abs grid" role="img" aria-label="Gallery of fifteen photographs: the doctor at work, at charity runs, events and press features">
    <div class="tile"></div><div class="tile"></div><div class="tile"></div><div class="tile"></div><div class="tile"></div>
    <div class="tile"></div><div class="tile"></div><div class="tile"></div><div class="tile"></div><div class="tile"></div>
    <div class="tile"></div><div class="tile"></div><div class="tile"></div><div class="tile"></div><div class="tile"></div>
  </div>
  <div class="abs load-more">LOAD MORE</div>
</section>

<section>
  <div class="abs testimonial"></div>
  <h2 class="abs section-head" style="top:3953px">What others say about me</h2>
  <blockquote class="abs t-quote">"Lorem ipsum dolor sit amet, consectetur adipiscing elit. Donec interdum facilisis nisi consectetur adipiscing elit."</blockquote>
  <div class="abs avatar" role="img" aria-label="Small portrait photograph of the reviewer"></div>
  <p class="abs t-name">Rena Malvik</p>
  <p class="abs t-role">Lorem Ipsum Jomatic</p>
</section>

<section>
  <div class="abs band" style="top:4232px">
    <h2 class="abs band-title">CONTACT</h2>
  </div>
  <div class="abs contact-bg"></div>
  <h2 class="abs section-head" style="top:4394px;left:81px;width:490px">CONTACT INFO</h2>
  <p class="abs contact-info">Vestibulum accumsan quis lectus pulvinar. Etiam sem quam, tempor sed lacus, vel tincidunt quis, sodales ac dui. Mauris efficitur tempor ac lorem, id commodo odio blandit nunc sed facilisis.</p>
  <dl class="abs contact-list">
    <dt>Email</dt><dd>drlucas@drlucasferrow.com</dd>
    <dt>Phone</dt><dd>+0(0)00 000 000</dd>
    <dt>Fax</dt><dd>+0(0)00 000 001</dd>
    <dt>Website</dt><dd>www.drlucasferrow.com</dd>
  </dl>
  <h2 class="abs section-head" style="top:4394px;left:649px;width:470px">SEND ME MESSAGE</h2>
  <form class="form">
    <label style="left:649px;top:4448px">Name</label><span class="field" style="left:649px;top:4492px;width:140px"></span>
    <label style="left:885px;top:4448px">Email Address</label><span class="field" style="left:885px;top:4492px;width:140px"></span>
    <label style="left:1055px;top:4448px">Subject</label><span class="field" style="left:1055px;top:4492px;width:64px"></span>
    <label style="left:649px;top:4522px">Message</label><span class="textarea" style="left:649px;top:4548px;width:470px;height:150px"></span>
  </form>
</section>

<footer class="abs footer">
  <p>© 2014 Dr. Lucas A Ferrow. All right is reserved</p>
  <div class="footer-links" aria-label="Profile links"><i></i><i></i><i></i><i></i><i></i><i></i><i></i><i></i></div>
</footer>

</body>
</html>
```